Website update for Mobile lighting company

We are looking to get a fresh look to our website and update it with some new products and services we are just starting to offer. We host there website through go daddy and use there website builder so we would like comparable files. The pages we would want are:
Home page
RUNE (one of our light tower units)
KT75 (one of our light tower units)
KT45 (one of our light tower units)
KT20 (one of our light tower units)
Service Page (would describe different serves we provide)
Contact Page with a google map
We would like to stick with our company colours and keep it clean and modern looking. Current website is www.brindlepower.ca

```html
<!DOCTYPE html>
<html lang="en">
<head>
<meta charset="utf-8">
<title>Brindle Power Services Corp.</title>
<link href="https://fonts.googleapis.com/css2?family=Raleway:wght@400;500;600;700&family=Arimo:wght@400;700&display=swap" rel="stylesheet">
<style>
:root{
  --lime:#b5bd1d;
  --ink:#3f3f3f;
  --muted:#8a8a8a;
  --navy:#2c4a7d;
  --link:#23407a;
  --hero-dark:#0b0b0d;
  --hero-soft:#23252e;
  --footer:#2a2a2a;
}
*{box-sizing:border-box;margin:0;padding:0}
html,body{width:850px;height:1200px;overflow:hidden;background:#fff}
body{position:relative;font-family:"Arimo",Arial,sans-serif;color:var(--ink)}
.abs{position:absolute}

/* header */
.site-header{position:absolute;left:0;top:0;width:850px;height:86px;border-top:2px solid var(--lime);border-bottom:1px solid var(--lime);background:#fff}
.brand{position:absolute;left:70px;top:28px;display:flex;align-items:center;gap:8px}
.brand-dot{width:26px;height:26px;border-radius:50%;background:var(--lime)}
.brand-name{font-family:"Raleway",sans-serif;font-weight:600;font-size:19px;color:var(--lime);letter-spacing:.5px}
.main-nav{position:absolute;top:-2px;left:361px;height:86px;display:flex}
.main-nav a{display:block;height:86px;line-height:86px;font-family:"Raleway",sans-serif;font-size:9.5px;color:#444;text-decoration:none;padding:0 15px;letter-spacing:.2px}
.main-nav a.active{background:var(--lime);color:#fff}

/* hero */
.hero{position:absolute;left:0;top:86px;width:850px;height:326px;background:linear-gradient(90deg,var(--hero-soft) 0,#15161c 35%,var(--hero-dark) 70%)}
.hero-copy{position:absolute;left:330px;top:195px;width:464px;text-align:center;color:#fff}
.hero-kicker{font-family:"Raleway",sans-serif;font-weight:500;font-size:21px;letter-spacing:.6px;line-height:26px}
.hero-title{font-family:"Raleway",sans-serif;font-weight:700;font-size:33px;line-height:40px;color:var(--lime);margin-top:6px;letter-spacing:.3px}
.hero-lede{font-family:"Raleway",sans-serif;font-size:9px;line-height:16px;margin-top:12px}
.hero-dots{position:absolute;left:734px;top:389px;display:flex;gap:3px}
.hero-dots span{width:10px;height:10px;border-radius:50%;border:2px solid #fff}
.hero-dots span.on{border-color:var(--lime)}
.hero-shadow{position:absolute;left:0;top:412px;width:850px;height:24px;background:radial-gradient(ellipse at 50% 0,rgba(0,0,0,.35),rgba(0,0,0,0) 70%)}

/* solution */
.section-title{font-family:"Raleway",sans-serif;font-weight:500;font-size:17.5px;color:#444;text-align:center;width:850px;left:0}
.section-sub{font-family:"Raleway",sans-serif;font-size:9.5px;color:var(--muted);text-align:center;width:850px;left:0}
.feature{position:absolute;width:170px;text-align:center}
.feature-badge{width:104px;height:104px;margin:0 auto;border-radius:50%;background:#f1f1f1;box-shadow:0 2px 4px rgba(0,0,0,.12);display:flex;align-items:center;justify-content:center}
.feature-badge .disc{width:86px;height:86px;border-radius:50%;background:var(--lime);display:flex;align-items:center;justify-content:center;box-shadow:0 3px 5px rgba(0,0,0,.25)}
.feature h3{font-family:"Raleway",sans-serif;font-weight:500;font-size:13px;color:#444;margin-top:12px}
.feature p{font-size:7.2px;line-height:14px;color:var(--muted);margin-top:9px}
.connector{position:absolute;top:547px;height:1px;background:#ddd;width:72px}
.connector i{position:absolute;left:33px;top:-2px;width:5px;height:5px;border-radius:50%;background:#8a8f2a}
.rule{position:absolute;left:0;width:850px;height:3px;background:#f2f2f2}

/* benefits */
.block-title{font-family:"Raleway",sans-serif;font-weight:500;font-size:17px;color:#444;padding-left:10px;border-left:4px double var(--lime);line-height:17px}
.tabs{position:absolute;left:70px;top:766px;width:424px;height:197px;border:1px solid #ddd}
.tab-bar{display:flex;height:27px;border-bottom:1px solid #ddd}
.tab-bar span{font-family:"Raleway",sans-serif;font-size:8px;color:#555;line-height:27px;text-align:center}
.tab-bar span.active{background:var(--navy);color:#fff;font-size:10px}
.tab-q{position:absolute;left:7px;top:43px;font-size:9px;color:var(--link)}
.tab-text{position:absolute;font-size:7.2px;line-height:14px;color:#777}
.tab-media{position:absolute;left:288px;top:41px;width:121px;height:81px;border:1px solid #ddd;padding:2px;background:#fff}
.tab-media div{width:100%;height:100%;background:linear-gradient(#1a1b1f,#0a0a0c)}
.btn{position:absolute;top:165px;height:19px;line-height:17px;font-size:7.5px;color:#444;border:1px solid #c9c9c9;border-radius:2px;background:linear-gradient(#fafafa,#e6e6e6);text-align:center}
.or{position:absolute;left:74px;top:169px;width:10px;height:10px;border-radius:50%;border:1px solid #bbb;background:#fff;font-size:6px;line-height:8px;text-align:center;z-index:1}

.challenge{position:absolute;left:515px;top:766px;width:265px;height:189px;border:1px solid #ddd}
.challenge-item{position:absolute;left:12px;width:245px}
.challenge-item .who{display:flex;align-items:center;gap:6px;font-size:8px;color:#333}
.challenge-item .who i{width:13px;height:13px;border-radius:50%;background:var(--lime)}
.challenge-item .lead{font-size:8px;color:var(--link);margin-top:6px}
.challenge-item p{font-size:7.2px;line-height:14px;color:#888;margin-top:3px}

/* about */
.about-text{position:absolute;left:110px;top:1055px;width:630px;text-align:center;font-size:7.2px;line-height:14.5px;color:#777}

/* footer */
.site-footer{position:absolute;left:0;top:1131px;width:850px;height:69px;background:var(--footer);border-bottom:3px solid var(--lime)}
.copyright{position:absolute;left:70px;top:30px;font-family:"Raleway",sans-serif;font-size:8px;color:#999}
.social{position:absolute;left:711px;top:24px;display:flex;gap:4px}
.social span{width:20px;height:20px;border-radius:50%;border:1px solid #777}
</style>
</head>
<body>

<header class="site-header">
  <div class="brand"><span class="brand-dot"></span><span class="brand-name">BRINDLE POWER</span></div>
  <nav class="main-nav">
    <a class="active" href="#">HOME</a>
    <a href="#">RUNE</a>
    <a href="#">KT75</a>
    <a href="#">KT45</a>
    <a href="#">KT20</a>
    <a href="#">SERVICES</a>
    <a href="#">CONTACT US</a>
  </nav>
</header>

<section class="hero" role="img" aria-label="Night photo of a yellow mobile light tower with a bright LED crown against a dark sky"></section>
<div class="hero-copy">
  <h1 class="hero-kicker">UNSURPASSED ILLUMINATION</h1>
  <h2 class="hero-title">BRINDLE POWER SERVICES</h2>
  <p class="hero-lede">Combines a sophisticated, yet obvious design with the latest technology to bring not only a safer<br>solution for illumination but an environmentally beneficial solution as well.</p>
</div>
<div class="hero-dots"><span></span><span class="on"></span><span></span><span></span></div>
<div class="hero-shadow"></div>

<h2 class="abs section-title" style="top:438px">OUR SOLUTION</h2>
<p class="abs section-sub" style="top:467px">Brindle Power Services Corp. has changed the way the drilling industry sees, literally.</p>

<div class="connector" style="left:210px"><i></i></div>
<div class="connector" style="left:387px"><i></i></div>
<div class="connector" style="left:565px"><i></i></div>

<div class="feature" style="left:73px;top:496px">
  <div class="feature-badge"><div class="disc">
    <svg width="44" height="44" viewBox="0 0 44 44" fill="none" stroke="#fff" stroke-width="3.5" stroke-linecap="round"><path d="M14 9a16 16 0 1 0 8-2"/><path d="M22 22l-6-7"/></svg>
  </div></div>
  <h3>self contained unit</h3>
  <p>Traditional location lighting requires multiple light towers throughout a location, gallons of diesel and can be labour intensive.</p>
</div>
<div class="feature" style="left:250px;top:496px">
  <div class="feature-badge"><div class="disc">
    <svg width="40" height="48" viewBox="0 0 40 48" fill="#fff"><path d="M20 3a14 14 0 0 0-8 25v6h16v-6A14 14 0 0 0 20 3zm-2 10h4v12h-4z"/><rect x="12" y="37" width="16" height="4" rx="1"/><rect x="15" y="43" width="10" height="3" rx="1"/></svg>
  </div></div>
  <h3>Environmental benefits</h3>
  <p>Traditional location lighting requires multiple light towers throughout a location, gallons of diesel and can be labour intensive.</p>
</div>
<div class="feature" style="left:426px;top:496px">
  <div class="feature-badge"><div class="disc">
    <svg width="46" height="44" viewBox="0 0 46 44" fill="#fff"><path d="M8 22l14 6v14L8 36z"/><path d="M24 28l14-6v14l-14 6z"/><path d="M8 20l15-6 15 6-15 6z"/><path d="M20 4 12 9l8 5V11a11 11 0 0 1 18 6h3A14 14 0 0 0 20 7z"/></svg>
  </div></div>
  <h3>Easy to install</h3>
  <p>Traditional location lighting requires multiple light towers throughout a location, gallons of diesel and can be labour intensive.</p>
</div>
<div class="feature" style="left:608px;top:496px">
  <div class="feature-badge"><div class="disc">
    <svg width="44" height="40" viewBox="0 0 44 40" fill="none" stroke="#fff" stroke-width="3.5" stroke-linejoin="round"><path d="M22 4 40 36H4z"/><path d="M22 15v10" stroke-linecap="round"/><circle cx="22" cy="30" r="1.2" fill="#fff"/></svg>
  </div></div>
  <h3>Better overall safety</h3>
  <p>Traditional location lighting requires multiple light towers throughout a location, gallons of diesel and can be labour intensive.</p>
</div>

<div class="rule" style="top:696px"></div>

<h2 class="abs block-title" style="left:72px;top:726px">OUR BENEFITS</h2>
<h2 class="abs block-title" style="left:517px;top:726px">OUR CHALLENGE</h2>

<div class="tabs">
  <div class="tab-bar">
    <span class="active" style="width:126px">ABOUT RUNE</span>
    <span style="width:98px">HOW IT WORKS</span>
    <span style="width:104px">CARBON CREDITS</span>
    <span style="width:94px">CONTACT US</span>
  </div>
  <div class="tab-q">WHAT IS RUNE CROWN MOUNT?</div>
  <p class="tab-text" style="left:8px;top:61px;width:270px">RUNE Crown Mount (RCM) is the most advanced on location lighting system and is engineered to secure directly to the crown of a derrick. The RUNE provides unsurpassed lighting capabilities ensuring a safe and well lit location. Traditional diesel and can be labour intensive.</p>
  <div class="tab-media" role="img" aria-label="Product photo of the crown mount LED ring, easy installation"><div></div></div>
  <p class="tab-text" style="left:8px;top:127px;width:410px">Top of the line North American manufactured LED lightning with a life expectancy of 100,000 hrs, making these LED systems reliable and reduce maintenance requirements......</p>
  <span class="btn" style="left:7px;width:70px">LEARN MORE</span>
  <span class="or">or</span>
  <span class="btn" style="left:81px;width:70px">VIEW MORE</span>
</div>

<div class="challenge">
  <div class="challenge-item" style="top:18px">
    <div class="who"><i></i>Brindle Power Services Corp.</div>
    <div class="lead">Traditional location lighting requires</div>
    <p>The RUNE CROWN MOUNT lighting system (patent pending) combines technology to bring not environmentally beneficial solution as well.</p>
  </div>
  <div style="position:absolute;left:0;top:100px;width:263px;height:1px;background:#ddd"></div>
  <div class="challenge-item" style="top:118px">
    <div class="who"><i></i>Brindle Power Services Corp.</div>
    <div class="lead">Traditional location lighting requires</div>
    <p>The RUNE CROWN MOUNT lighting system (patent pending) combines technology to bring not environmentally beneficial solution as well.</p>
  </div>
</div>

<div class="rule" style="top:992px"></div>

<h2 class="abs section-title" style="top:1021px">ABOUT BRINDLE POWER</h2>
<p class="about-text">The RUNE CROWN MOUNT lighting system (patent pending) combines a sophisticated, yet obvious design with the latest technology to bring not only a safer solution for illumination but an environmentally beneficial solution as well. The RUNE CROWN MOUNT lighting system (patent pending) combines a sophisticated, yet obvious design with the latest technology to bring not only a safer solution for illumination but an environmentally beneficial solution as well.</p>

<footer class="site-footer">
  <p class="copyright">Copyright © 2015 Brindle Power Services Corp All rights reserved.</p>
  <div class="social" aria-label="Social links"><span></span><span></span><span></span></div>
</footer>

</body>
</html>
```